Bright Horizon Painting and Remodeling needs a business card

Business card should have company logo. I will upload two different logos and let me see which one is a better design for the business card.

Name of company: Bright Horizon Painting and Remodeling
Address: 4126 NW 71st st Suite 214
Miami, FL 33166

local phone: (305) 555-0142
toll free (855) 555-0197
fax (866) 555-0163

email: corinne@paintingbrighthorizon.example

not sure if i should include social media links or names on the business card.

company does interior and exterior painting, pressure washing, wall paper removal, drywall and stucco repair, staining,

We give free estimates.

I want a two sided business card.

Not sure if all this information is necessary for the business card. Designer can pick out whatever information they deem is important for a consumer to see on the business card.

Anticipating on the business card to be printed on nice quality.

I will upload an image of one of the logos on a type of business card surface. That idea can be used as well. Be creative. Business card should be professional but very nice and eye catching.

remove drywall and stucco repair and replace with tile installation

Industry/Entity Type

Business

Contact Information for Business Card

Miami, FL 33166

toll free (855) 555-0197
fax (866) 555-0163

company does interior and exterior painting, pressure washing, wall paper removal, drywall and stucco repair, staining, tile removal, *specializing in vinyl floor removal

free estimates.

Requirements
Must have
• Profesional font

```html
<!DOCTYPE html>
<html lang="en">
<head>
<meta charset="utf-8">
<title>Bright Horizon Painting and Remodeling – Business Card</title>
<link rel="stylesheet" href="https://fonts.googleapis.com/css2?family=Open+Sans:wght@400;600;700&display=swap">
<style>
  :root {
    --page-bg: #e9e6e1;
    --card-light: #ffffff;
    --card-dark: #3b3b3b;
    --ink-dark: #222222;
    --ink-light: #ffffff;
    --dot-pink: #e4607f;
    --dot-purple: #8e63c9;
    --dot-teal: #4fa8b5;
    --dot-green: #6cc25c;
    --dot-yellow: #f2d36b;
    --brand-ink-light: #2a2a2a;
    --brand-ink-dark: #ffffff;
    --card-shadow: 0 10px 28px rgba(0,0,0,0.22);
  }
  * { box-sizing: border-box; margin: 0; padding: 0; }
  html, body { width: 1200px; height: 900px; overflow: hidden; }
  body {
    background: var(--page-bg);
    font-family: "Open Sans", Arial, sans-serif;
    position: relative;
  }
  .card {
    position: absolute;
    width: 540px;
    height: 309px;
    border-radius: 4px;
    box-shadow: var(--card-shadow);
    overflow: hidden;
  }
  .card--front { left: 40px; top: 296px; background: var(--card-light); color: var(--ink-dark); }
  .card--back  { left: 620px; top: 296px; background: var(--card-dark); color: var(--ink-light); }

  /* Services list */
  .services {
    position: absolute; left: 262px; top: 30px;
    list-style: none; font-size: 13px; font-weight: 600; line-height: 1.75;
  }
  .services li { display: flex; align-items: center; gap: 9px; }
  .services li::before {
    content: ""; width: 8px; height: 8px; border-radius: 50%;
    background: var(--dot); flex: none;
  }

  /* Brand name block in place of the mark */
  .brand {
    position: absolute;
    display: flex; align-items: center; gap: 12px;
    font-weight: 700; text-transform: uppercase; letter-spacing: 0.06em;
    line-height: 1.15;
  }
  .brand__dot { width: 26px; height: 26px; border-radius: 50%; flex: none; }
  .card--front .brand { left: 44px; top: 178px; font-size: 19px; color: var(--brand-ink-light); }
  .card--front .brand__dot { background: var(--dot-purple); }
  .card--back .brand { left: 36px; top: 186px; font-size: 17px; color: var(--brand-ink-dark); }
  .card--back .brand__dot { background: var(--dot-teal); }

  /* Back side contact */
  .contact-name {
    position: absolute; left: 236px; top: 36px;
    font-size: 19px; font-weight: 700; letter-spacing: 0.04em;
  }
  .contact-lines {
    position: absolute; left: 238px; top: 76px;
    list-style: none; font-size: 12.5px; line-height: 1.6;
  }
  .contact-lines li { display: flex; align-items: center; gap: 7px; white-space: nowrap; }
  .contact-lines svg { width: 12px; height: 12px; fill: var(--ink-light); flex: none; }
  .address {
    position: absolute; left: 340px; top: 196px;
    font-size: 12.5px; line-height: 1.5; font-style: normal;
  }
  .toll-free {
    position: absolute; left: 340px; top: 248px;
    font-size: 13px; font-weight: 400;
  }
  .toll-free strong { font-weight: 700; letter-spacing: 0.03em; }
</style>
</head>
<body>

  <section class="card card--front" aria-label="Card front">
    <ul class="services">
      <li style="--dot: var(--dot-pink)">Interior And Exterior Painting</li>
      <li style="--dot: var(--dot-purple)">Pressure Washing</li>
      <li style="--dot: var(--dot-teal)">Wall Paper Reomval</li>
      <li style="--dot: var(--dot-green)">Drywall and Stucco Repair</li>
      <li style="--dot: var(--dot-yellow)">Staining</li>
    </ul>
    <div class="brand">
      <span class="brand__dot"></span>
      <span>Bright Horizon<br>Painting and Remodeling</span>
    </div>
  </section>

  <section class="card card--back" aria-label="Card back">
    <h1 class="contact-name">CORINNE</h1>
    <ul class="contact-lines">
      <li>
        <svg viewBox="0 0 16 16" aria-hidden="true"><path d="M3.6 1.2l2.3 2.6-1.3 1.8c.9 2 2.6 3.7 4.6 4.6l1.8-1.3 2.6 2.3-1.4 2.4C6.4 13.2 2.8 9.6 1.2 3.8z"/></svg>
        317.555.0128
      </li>
      <li>
        <svg viewBox="0 0 16 16" aria-hidden="true"><path d="M4 1h6l2 2v3h1.5c.8 0 1.5.7 1.5 1.5V14c0 .6-.4 1-1 1H2c-.6 0-1-.4-1-1V7.5C1 6.7 1.7 6 2.5 6H4zm1 1v4h6V3.5L9.5 2zM4 9v1.5h8V9zm0 2.5V13h8v-1.5z"/></svg>
        317.555.0176
      </li>
      <li>
        <svg viewBox="0 0 16 16" aria-hidden="true"><path d="M1 3h14v10H1zm1.5 1.2v.3L8 8.6l5.5-4.1v-.3zm0 2.1v5.4h11V6.3L8 10.4z"/></svg>
        corinne@paintingbrighthorizon.example
      </li>
    </ul>
    <div class="brand">
      <span class="brand__dot"></span>
      <span>Bright Horizon<br>Painting and<br>Remodeling</span>
    </div>
    <address class="address">4126 NW 71st st Suite 214<br>Miami, FL 33166</address>
    <p class="toll-free"><strong>TOLL FREE</strong> (855) 555-0197</p>
  </section>

</body>
</html>
```